Uitnodiging van het huwelijk
doelgroep
Uitnodiging voor onze bruiloft voor vrienden en familie
Conceptuele formulering
Wij willen hutten individuele uitnodigingskaart. Het moet iets bijzonders zijn, dwz straalt iets bijzonders, maar anders vrij eenvoudig en modern en niet cheesy! Op de voorkant van onze huwelijksdatum en onze namen moeten eventueel een foto van ons. misschien zelfs een citaat: "Het geluk is het enige dat verdubbelt als je het (Gerold Pankmüller) Uitnodiging voor onze kerk bruiloft misschien een motief, wat doe je het citaat past delen ....

```html
<!DOCTYPE html>
<html lang="de">
<head>
<meta charset="utf-8">
<title>Hochzeitseinladung – Wir heiraten!</title>
<link rel="stylesheet" href="https://fonts.googleapis.com/css2?family=Pinyon+Script&family=Mulish:wght@300&display=swap">
<style>
  :root {
    --mint: #a1d8cb;
    --mint-line: #9dd6c9;
    --ink: #1e1a1a;
    --paper: #ffffff;
  }
  * { margin: 0; padding: 0; box-sizing: border-box; }
  html, body { width: 1200px; height: 600px; overflow: hidden; background: var(--paper); }
  .card {
    position: relative;
    width: 1200px;
    height: 600px;
    background: var(--paper);
    font-family: "Mulish", "Helvetica Neue", Arial, sans-serif;
    font-weight: 300;
  }
  .fold-line {
    position: absolute;
    left: 599px;
    width: 0;
    border-left: 2px dotted var(--mint-line);
  }
  .fold-line--top { top: 0; height: 144px; }
  .fold-line--bottom { top: 440px; height: 160px; }
  .band {
    position: absolute;
    left: 0; top: 144px;
    width: 1200px; height: 296px;
    background: var(--mint);
    border-top: 2px dotted #c3e6de;
    border-bottom: 2px dotted var(--mint-line);
  }
  .script {
    position: absolute;
    font-family: "Pinyon Script", cursive;
    font-weight: 400;
    color: var(--ink);
    line-height: 1;
    white-space: nowrap;
  }
  .script--ja { left: 232px; top: 60px; font-size: 150px; }
  .script--headline { left: 664px; top: 70px; font-size: 96px; }
  .text-box {
    position: absolute;
    border: 2px dotted var(--paper);
    color: var(--paper);
    text-align: center;
    font-size: 15.5px;
    line-height: 17.8px;
  }
  .text-box--quote { left: 180px; top: 246px; width: 272px; height: 81px; padding-top: 4px; }
  .text-box--details { left: 685px; top: 247px; width: 399px; height: 106px; padding-top: 4px; }
  .text-box--details p + p { margin-top: 17.8px; }
  .envelope { position: absolute; left: 866px; top: 457px; width: 38px; height: 21px; }
  .contact {
    position: absolute;
    left: 758px; top: 483px;
    width: 253px; height: 83px;
    border: 2px dotted var(--mint-line);
    color: var(--mint-line);
    text-align: center;
    font-size: 13px;
    line-height: 15.3px;
    padding-top: 1px;
  }
  .hearts { position: absolute; left: 236px; top: 476px; width: 154px; height: 88px; }
</style>
</head>
<body>
<main class="card">
  <div class="fold-line fold-line--top"></div>
  <div class="fold-line fold-line--bottom"></div>
  <div class="band"></div>

  <h1 class="script script--ja">Ja</h1>
  <h2 class="script script--headline">Wir heiraten!</h2>

  <div class="text-box text-box--quote">
    <p>Zusammen durch die Welt zu gehen ist schöner, als allein zu stehen. Und sich darauf das Wort zu geben ist wohl das Schönste im Leben.</p>
  </div>

  <div class="text-box text-box--details">
    <p>Am … um … läuten für uns die Hochzeitsglocken in …</p>
    <p>Daran anschließend werden wir im Hotel … erwartet, wo wir gemeinsam diesen Tag zu unserer schönsten Erinnerung werden lassen möchten.</p>
  </div>

  <svg class="hearts" viewBox="0 0 154 88" aria-hidden="true">
    <path d="M40 86 C30 72 4 58 2 38 C0 16 12 2 28 2 C40 2 46 12 48 18 C52 8 60 2 72 2 C82 2 88 6 90 14"
          fill="none" stroke="var(--mint-line)" stroke-width="1"/>
    <path d="M40 86 C48 76 56 70 62 66" fill="none" stroke="var(--mint-line)" stroke-width="1"/>
    <path d="M95 86 C84 72 56 64 54 42 C52 18 62 4 78 4 C92 4 100 14 102 22 C106 12 114 4 128 4 C144 4 152 18 152 36 C152 60 112 70 95 86 Z"
          fill="var(--mint-line)"/>
  </svg>

  <svg class="envelope" viewBox="0 0 38 21" aria-hidden="true">
    <rect x="0" y="0" width="38" height="21" fill="var(--mint-line)"/>
    <path d="M1 1 L19 13 L37 1 M1 20 L15 10 M37 20 L23 10" fill="none" stroke="var(--paper)" stroke-width="1.2"/>
  </svg>

  <address class="contact" style="font-style: normal;">
    Lena und Jonas Birkfeld<br>
    Lindenweg 24b<br>
    82041 Lindental<br>
    07131-4860273<br>
    lj.birkfeld@beispiel.de
  </address>
</main>
</body>
</html>
```